Business Card & Logo

Business Card Design Project & Logo

Need logo for business card

Company name is ZORVA electric bikes USA

Target Market(s)

Consumer

Industry/Entity Type

Sporting Good

Contact Information for Business Card

Electric Bike Business Cards, Flyers, and LOGO.

Font styles to use
Sans Serif

Colors
ffc214
ffcf3e
faa54b
fee18a
f37122

Requirements
Must have
• New look &LOGO

```html
<!DOCTYPE html>
<html lang="en">
<head>
<meta charset="utf-8">
<title>ZORVA Electric Bikes USA – Business Card</title>
<link href="https://fonts.googleapis.com/css2?family=Jost:wght@400;500;600&display=swap" rel="stylesheet">
<style>
  :root {
    --bg: #f9a54b;
    --card-orange: #f37122;
    --card-yellow: #ffcf3e;
    --ink: #111111;
    --white: #ffffff;
    --rule: #f7b23a;
  }
  html, body {
    margin: 0;
    padding: 0;
    width: 1200px;
    height: 1200px;
    overflow: hidden;
    background: var(--bg);
    font-family: "Jost", "Futura", sans-serif;
  }
  .canvas {
    position: relative;
    width: 1200px;
    height: 1200px;
  }
  .card {
    position: absolute;
    background: var(--card-orange);
  }
  .card--front { left: 344px; top: 248px; width: 518px; height: 296px; }
  .card--back  { left: 344px; top: 638px; width: 520px; height: 295px; }

  .brand-name {
    position: absolute;
    left: 0; right: 0;
    text-align: center;
    color: var(--white);
    font-weight: 600;
    margin: 0;
  }
  .tagline {
    position: absolute;
    left: 0; right: 0;
    text-align: center;
    color: var(--white);
    font-weight: 400;
    margin: 0;
  }
  .card--front .brand-name { top: 52px; font-size: 38px; letter-spacing: 14px; text-indent: 14px; }
  .card--front .tagline { top: 116px; font-size: 24px; }

  .info-panel {
    position: absolute;
    left: 16px; top: 148px;
    width: 488px; height: 132px;
    background: var(--card-yellow);
  }
  .office {
    position: absolute;
    left: 0; top: 14px;
    width: 164px;
    text-align: center;
    color: var(--ink);
  }
  .office__name {
    margin: 0;
    font-weight: 600;
    font-size: 15px;
    line-height: 20px;
    letter-spacing: 1px;
  }
  .office__address {
    margin: 6px 0 0;
    font-size: 15px;
    line-height: 20px;
  }
  .divider {
    position: absolute;
    left: 154px; top: 12px;
    width: 2px; height: 108px;
    background: var(--rule);
  }
  .contact-list {
    position: absolute;
    left: 170px; top: 10px;
    margin: 0; padding: 0;
    list-style: none;
  }
  .contact-list li {
    display: flex;
    align-items: center;
    height: 40px;
    font-size: 18px;
    color: var(--ink);
  }
  .contact-list svg {
    width: 30px; height: 30px;
    margin-right: 18px;
    flex: none;
  }

  .back-panel {
    position: absolute;
    left: 15px; top: 14px;
    width: 487px; height: 265px;
    background: var(--card-yellow);
  }
  .card--back .brand-name { top: 14px; font-size: 54px; letter-spacing: 30px; text-indent: 30px; }
  .mark-dot {
    position: absolute;
    left: 186px; top: 96px;
    width: 116px; height: 116px;
    border-radius: 50%;
    border: 8px solid var(--card-orange);
    box-sizing: border-box;
  }
  .card--back .tagline { top: 222px; font-size: 34px; }
</style>
</head>
<body>
<div class="canvas">

  <section class="card card--front">
    <h1 class="brand-name">ZORVA</h1>
    <p class="tagline">Electric Bikes USA</p>

    <div class="info-panel">
      <div class="office">
        <p class="office__name">ZORVA<br>ELECTRIC BIKES<br>USA - DENVER</p>
        <p class="office__address">2480 Larkspur Ave,<br>Denver, CO 80211</p>
      </div>
      <div class="divider"></div>
      <ul class="contact-list">
        <li>
          <svg viewBox="0 0 30 30" aria-hidden="true">
            <path d="M2 14 L28 3 L18 28 L14 17 Z" fill="#111"/>
            <path d="M14 17 L28 3" stroke="#ffcf3e" stroke-width="1.5"/>
          </svg>
          ZorvaBikes@zorvaelectric.com
        </li>
        <li>
          <svg viewBox="0 0 30 30" aria-hidden="true" fill="none" stroke="#111" stroke-width="1.8">
            <circle cx="14" cy="14" r="11"/>
            <ellipse cx="14" cy="14" rx="5" ry="11"/>
            <path d="M3 14 H25 M5 8 H23 M5 20 H23"/>
            <path d="M19 18 L28 23 L23 24 L21 29 Z" fill="#111" stroke="#ffcf3e" stroke-width="1"/>
          </svg>
          www.ZorvaBikesUSA.com
        </li>
        <li>
          <svg viewBox="0 0 30 30" aria-hidden="true">
            <circle cx="15" cy="15" r="13" fill="none" stroke="#111" stroke-width="2"/>
            <path d="M10 8 L13 8 L14 12 L12 13.5 Q14 17 16.5 18 L18 16 L22 17 L22 20 Q21 22 18 22 Q10 20 8 12 Q8 9 10 8 Z" fill="#111"/>
          </svg>
          (720) 555-0142
        </li>
      </ul>
    </div>
  </section>

  <section class="card card--back">
    <div class="back-panel">
      <h2 class="brand-name">ZORVA</h2>
      <div class="mark-dot"></div>
      <p class="tagline">Electric Bikes USA</p>
    </div>
  </section>

</div>
</body>
</html>
```